Sports Picks Site

I'm looking to design a simple sports betting site. My site is currently here: www.quartzlanetips.example.net

I'd like it to be a wordpress site that is layed out very similar to this site: www.oddsmarlow.example.

What I need:
1-News Section
2-Rankings
3-Sportsbook Section

Please let me know if you have any questions.

Thanks,
Tobin

```html
<!DOCTYPE html>
<html lang="en">
<head>
<meta charset="utf-8">
<title>Streakblaze</title>
<link rel="stylesheet" href="https://fonts.googleapis.com/css2?family=Ubuntu:ital,wght@0,400;0,500;0,700;1,700&display=swap">
<style>
:root{
  --page:#0b0b0b;
  --panel:#000;
  --card:#1e1e1e;
  --card-line:#4a4a4a;
  --yellow:#fdd72a;
  --orange:#f7941d;
  --red:#ff2a1a;
  --text:#f2f2f2;
  --feed:#9fe0e6;
  --link:#b0120a;
}
*{box-sizing:border-box;margin:0;padding:0}
html,body{width:1185px;height:1200px;overflow:hidden;background:var(--page)}
body{position:relative;font-family:Arial,Helvetica,sans-serif;color:var(--text)}
.abs{position:absolute}
.backdrop{left:0;top:0;width:1185px;height:1200px;background:linear-gradient(90deg,#3a3a3a 0%,#1a1a1a 12%,#0b0b0b 30%,#0b0b0b 70%,#1a1a1a 88%,#3a3a3a 100%)}
.brand{left:0;width:1185px;top:30px;text-align:center;font-family:Ubuntu,sans-serif;font-weight:700;font-size:46px;color:var(--orange);letter-spacing:1px}
.rules{left:0;width:1185px;top:101px;text-align:center;font-family:Ubuntu,sans-serif;font-weight:500;font-size:14px;line-height:18px;color:#fff}
.flames{left:149px;top:176px;width:889px;height:102px;background:linear-gradient(0deg,#ff9a1a 0%,#e0420c 35%,#7a1a04 70%,rgba(0,0,0,0) 100%)}
.slogan{left:149px;width:889px;top:212px;text-align:center;font-family:Ubuntu,sans-serif;font-style:italic;font-weight:700;font-size:26px;color:#fff;letter-spacing:1px}
.panel{left:149px;top:278px;width:889px;height:882px;background:var(--panel);border-top:3px solid var(--orange)}
.nav{left:168px;top:298px;width:852px;height:43px;background:var(--yellow);font-family:Ubuntu,sans-serif;font-weight:500;font-size:14px;color:#111}
.nav a{position:absolute;top:13px;transform:translateX(-50%);color:#111;text-decoration:none;white-space:nowrap}
.nav a.current{color:#e8300c;border-bottom:2px solid #e8300c;padding:0 4px 1px}
.photo{background:linear-gradient(110deg,#e9e9e9 0%,#9a9a9a 45%,#b8312a 60%,#6d1d18 100%)}
.hero{left:168px;top:360px;width:418px;height:200px;border:1px solid #555;background:#2a2a2a}
.hero .photo{position:absolute;left:13px;top:12px;width:391px;height:174px}
.headline{left:183px;top:567px;width:390px;font-family:Ubuntu,sans-serif;font-weight:400;font-size:17px;line-height:20px;color:#fff}
.rule-y{height:2px;background:var(--yellow)}
.story{left:183px;top:628px;width:380px;font-size:11.5px;line-height:16.7px;color:#eee}
.story a{color:var(--yellow)}
.thumb{top:763px;width:204px;height:125px;border:1px solid #555;background:#1c1c1c}
.thumb .photo{position:absolute;left:12px;top:10px;width:178px;height:103px}
.posts{top:906px;width:204px;height:190px;font-size:11px;line-height:16.7px;list-style:none}
.posts li{position:absolute;left:0;width:204px;padding-left:20px}
.posts li+li{border-top:1px solid #2c2c2c;padding-top:17px}
.posts li::before{content:"";position:absolute;left:1px;top:5px;border-left:5px solid #fff;border-top:3px solid transparent;border-bottom:3px solid transparent}
.posts li+li::before{top:22px}
.posts li.hot{color:var(--yellow)}
.btn{height:23px;background:var(--yellow);color:#111;font-size:11.5px;text-align:center;line-height:23px}
.ranks{left:601px;top:360px;width:193px;height:770px;background:var(--card);border:1px solid var(--card-line);overflow:hidden}
.ranks h2{font-family:Ubuntu,sans-serif;font-weight:400;font-size:17px;line-height:20px;text-align:center;margin-top:8px;color:#fff}
.ranks .rule-y{margin:8px 6px 0}
.ranks p{font-size:11px;line-height:16.7px;color:#ddd;padding:4px 8px 0;height:71px}
.ranks ul{list-style:none;padding:0 6px}
.ranks li{height:27.8px;line-height:27.8px;display:flex;justify-content:space-between;border-bottom:1px solid #3c3c3c;font-size:11.5px;font-weight:700;color:#fff;padding:0 2px}
.ranks li:last-child{border-bottom:0}
.l1{color:var(--yellow);font-weight:400}
.l2{color:var(--orange);font-weight:400}
.l3{color:var(--red);font-weight:400}
.social{top:359px;width:42px;height:41px;font-size:8px;font-weight:700;color:#fff;display:flex;align-items:center;justify-content:center;text-align:center}
.side{left:807px;top:413px;width:213px;height:717px;background:var(--card);border:1px solid var(--card-line)}
.side-head{left:807px;top:413px;width:213px;height:44px;background:var(--yellow);font-family:Ubuntu,sans-serif;font-size:17px;color:#222;text-align:center;line-height:44px}
.label{font-size:11px;color:#eee}
.book{width:71px;height:23px;background:#3a3a3a;font-size:12px;font-weight:700;color:#ddd;text-align:center;line-height:23px}
.offer{font-size:11px;color:#eee;white-space:nowrap}
.bonus{font-size:11px;font-weight:700;color:var(--yellow);white-space:nowrap}
.feed{left:819px;top:622px;width:191px;height:498px;background:var(--feed)}
.feed-title{left:819px;top:636px;width:191px;text-align:center;font-family:Ubuntu,sans-serif;font-weight:700;font-size:24px;color:#fff}
.stamp{left:826px;width:177px;text-align:right;font-size:9px;color:#fff}
.tweet{left:826px;width:177px;background:#fff;color:#333;font-size:10px;line-height:16.7px;padding:4px 6px;overflow:hidden}
.tweet .ava{float:left;width:46px;height:46px;margin:2px 6px 2px 0;background:radial-gradient(circle,#d2691e 0%,#5a2308 60%,#111 100%)}
.tweet .ava.person{background:linear-gradient(180deg,#8a8a70,#3a3a30)}
.tweet b{color:#222}
.tweet .h{color:#999;font-size:9px}
.tweet u{color:var(--link)}
.foot-line{left:149px;top:1158px;width:889px;height:3px;background:var(--orange)}
.copy{left:0;width:1185px;top:1179px;text-align:center;font-size:11px;color:#555}
</style>
</head>
<body>
<div class="abs backdrop" role="img" aria-label="Dark stadium backdrop with football players at the sides"></div>

<div class="abs brand">Streakblaze</div>
<div class="abs rules">1 - Submit One Spread or Total Pick a Day.<br>2 - Achieve a 5 Game Win Streak.<br>3 - Become the Featured Handicapper at Streakblaze.</div>

<div class="abs flames" role="img" aria-label="Band of flames"></div>
<div class="abs slogan">Respect the Streak!</div>

<div class="abs panel"></div>

<nav class="abs nav">
  <a style="left:140px">HOME</a>
  <a style="left:297px">SUBMIT PICK</a>
  <a class="current" style="left:486px">HOW IT WORKS</a>
  <a style="left:663px">CONTACT US</a>
</nav>

<div class="abs hero"><div class="photo" role="img" aria-label="Two football players in opposing team uniforms"></div></div>
<h1 class="abs headline">Dale Corwin, Nate Holloway make up for Ironmen's flaws</h1>
<div class="abs rule-y" style="left:183px;top:616px;width:390px"></div>
<div class="abs story">
  <p>The 3-3 Harbor City Ironmen have the look and feel of an 8-8 team. They're banged up, depleted. They've lost to inferior opponents. Individual players have grossly underachieved. But they're still legit contenders.</p>
  <p style="margin-top:16.7px">In a wide-open and weak East Conference, the Ironmen have a chance to make something happen for two reasons: They have coach Dale Corwin and quarterback Nate Holloway on their side... <a>read more</a></p>
</div>

<div class="abs thumb" style="left:168px"><div class="photo" role="img" aria-label="Football tackle during a game" style="background:linear-gradient(160deg,#5a6a8a,#4c7a3a 60%,#d8d8d8)"></div></div>
<div class="abs thumb" style="left:382px"><div class="photo" role="img" aria-label="Two football helmets facing a championship trophy" style="background:linear-gradient(120deg,#1d2a5a,#5a6a9a 50%,#c8c8c8)"></div></div>

<ul class="abs posts" style="left:168px">
  <li style="top:0">Monday Night Wrap Up</li>
  <li class="hot" style="top:27px">PL Week 8 Picks: Reed Callow 61-27 Record Last 30 Days</li>
  <li style="top:80px">3 Reasons Why Corsairs Will Upset The Northmen Thursday Night</li>
  <li style="top:132px">CAUTION HOT: We are closing in on another streak</li>
</ul>
<ul class="abs posts" style="left:382px">
  <li style="top:0">The flame is burning bright.</li>
  <li style="top:27px">Vegas Showing Brackwater Tech No Respect As 24 Point Dog</li>
  <li style="top:80px">WE have fire! 5 for 5.</li>
  <li style="top:132px">Vegas Showing Brackwater Tech No Respect As 24 Point Dog</li>
</ul>
<div class="abs btn" style="left:273px;top:1107px;width:86px">more posts</div>
<div class="abs btn" style="left:488px;top:1107px;width:86px">more posts</div>

<section class="abs ranks">
  <h2>STREAKBLAZE<br>RANKINGS</h2>
  <div class="rule-y"></div>
  <p>A handicapper earns a level by achieving a 5 game streak. The level is lost with a 4 game losing streak</p>
  <ul>
    <li>@slateb54<span class="l2">LEVEL 2</span></li>
    <li>@FirstLine<span class="l3">LEVEL 3</span></li>
    <li>@crewcashstackcc<span class="l3">LEVEL 3</span></li>
    <li>@islandgreen420<span class="l1">LEVEL 1</span></li>
    <li>@slateb54<span class="l2">LEVEL 2</span></li>
    <li>@FirstLine<span class="l1">LEVEL 1</span></li>
    <li>@crewcashstackcc<span class="l1">LEVEL 1</span></li>
    <li>@islandgreen420<span class="l3">LEVEL 3</span></li>
    <li>@slateb54<span class="l2">LEVEL 2</span></li>
    <li>@FirstLine<span class="l2">LEVEL 2</span></li>
    <li>@crewcashstackcc<span class="l2">LEVEL 2</span></li>
    <li>@islandgreen420<span class="l3">LEVEL 3</span></li>
    <li>@slateb54<span class="l1">LEVEL 1</span></li>
    <li>@FirstLine<span class="l1">LEVEL 1</span></li>
    <li>@crewcashstackcc<span class="l1">LEVEL 1</span></li>
    <li>@islandgreen420<span class="l2">LEVEL 2</span></li>
    <li>@slateb54<span class="l1">LEVEL 1</span></li>
    <li>@FirstLine<span class="l3">LEVEL 3</span></li>
    <li>@crewcashstackcc<span class="l3">LEVEL 3</span></li>
    <li>@slateb54<span class="l1">LEVEL 1</span></li>
    <li>@FirstLine<span class="l2">LEVEL 2</span></li>
    <li>@crewcashstackcc<span class="l2">LEVEL 2</span></li>
    <li>@islandgreen420<span class="l2">LEVEL 2</span></li>
  </ul>
</section>

<div class="abs social" style="left:807px;background:#3b5ea8">Social</div>
<div class="abs social" style="left:865px;background:#2aa7df">Chirp</div>
<div class="abs social" style="left:923px;background:#f39c1a">Feed</div>
<div class="abs social" style="left:979px;background:#d92b25">Video</div>

<div class="abs side"></div>
<div class="abs side-head">WHERE WE PLAY</div>
<div class="abs label" style="left:818px;top:469px">Sportsbook:</div>
<div class="abs book" style="left:819px;top:495px">linepost</div>
<div class="abs offer" style="left:896px;top:501px">- Linepost</div>
<div class="abs bonus" style="left:947px;top:501px">50% Bonus</div>
<div class="abs" style="left:895px;top:537px;width:108px;height:1px;background:#555"></div>
<div class="abs label" style="left:818px;top:549px">Sportsbook:</div>
<div class="abs book" style="left:819px;top:575px">oddsway</div>
<div class="abs offer" style="left:896px;top:581px">- Oddsway</div>
<div class="abs bonus" style="left:947px;top:581px">20% Bonus</div>

<div class="abs feed"></div>
<div class="abs feed-title">Chirpline</div>

<div class="abs stamp" style="top:679px">16 min</div>
<div class="abs tweet" style="top:692px;height:137px"><div class="ava" role="img" aria-label="Football on fire avatar"></div><b>Streakblaze</b> <span class="h">@Streakblaze</span> What's your winning pick for today's <u>#hawks</u> vs <u>#ospreys</u> game? Achieve a 5 win streak and become our featured handicapper.What's your winning pick for today's #hawks vs #ospreys game?</div>

<div class="abs stamp" style="top:841px">9 min</div>
<div class="abs tweet" style="top:854px;height:91px"><div class="ava person" role="img" aria-label="Profile photo"></div><b>ellis brand</b> <span class="h">@ellisbrand1</span> <u>@Streakblaze</u> learning towards the ospreys. coach Hale it's 13-0 coming off a bye week.</div>

<div class="abs stamp" style="top:954px">1 min</div>
<div class="abs tweet" style="top:967px;height:107px"><div class="ava" role="img" aria-label="Football on fire avatar"></div><b>Streakblaze</b> <span class="h">@Streakblaze</span> What's your winner for today's <u>#rangers</u> vs <u>#ironmen</u> game? Become our featured handicapper by winning 5 picks in a row.</div>

<div class="abs btn" style="left:901px;top:1085px;width:100px">view all tweets</div>

<div class="abs foot-line"></div>
<div class="abs copy">Copyright © 2012 · streakblaze.example</div>
</body>
</html>
```